Klenvo Disinfecting company

Company name: Klenvo Inc
We are starting up a new company that is a professional spray disinfecting company. We will be offering a service where we go into facilities like residential, office, child care, medical, dental, restaurant, entertainment, hotel/motel, automotive fleets with professional spraying equipment and disinfect their facilities for a fee. Our products kills a wide range of viruses and pathogens including Covid 19.

Target Market(s)

Residential, commercial office space, child care, medical, dental, restaurant, entertainment facilities, hotel/motel, automotive fleets.

Font styles to use
Sans Serif

Colors
31b7a3

Requirements
Must have
• Company name - Klenvo Inc
Phone - 905-487-2963
Email - klenvotrue@mailbox-example.com
Our Slogan - Disinfect Today For A Safe Tomorrow
Brief description of our reservice
Nice to have
• Some kind of a picture of a man with a sprayer, perhaps in a white coveralls, perhaps on a background of a few of the facilities in mention in my target market section. I have uploaded 4 examples of print ads form similar companies. I don't necessarily want them to look alike however these are very professional ads and will give you the gist of what I'm looking for.

```html
<!DOCTYPE html>
<html lang="en">
<head>
<meta charset="utf-8">
<title>Klenvo Inc – Disinfecting Services Flyer</title>
<link rel="stylesheet" href="https://fonts.googleapis.com/css2?family=Bebas+Neue&family=Fira+Sans:wght@400;500;600;700&family=Lato:wght@400;700&display=swap">
<style>
  :root {
    --teal: #31b7a3;
    --teal-deep: #289a89;
    --teal-text: #2aa894;
    --green: #8cc63f;
    --green-soft: #a3d160;
    --ink: #3c3f44;
    --ink-soft: #55585d;
    --paper: #ffffff;
    --backdrop: #e9ebee;
    --sky-1: #8fbfe6;
    --sky-2: #d3e5f3;
    --roof: #6f7c8c;
    --wall: #a9b3bd;
    --lamp: #d9b486;
    --suit: #eef2f6;
  }
  * { box-sizing: border-box; margin: 0; padding: 0; }
  html, body { width: 1200px; height: 940px; overflow: hidden; background: var(--backdrop); }
  .flyer {
    position: absolute; left: 252px; top: 20px;
    width: 696px; height: 900px;
    background: var(--paper);
    box-shadow: 0 6px 24px rgba(0,0,0,.18);
    overflow: hidden;
    font-family: "Lato", sans-serif;
  }
  .artwork { position: absolute; inset: 0; width: 696px; height: 900px; }

  .brand {
    position: absolute; left: 37px; top: 34px;
    display: flex; align-items: center; gap: 10px;
    font-family: "Fira Sans", sans-serif; font-weight: 500;
    font-size: 50px; letter-spacing: .5px; color: var(--teal);
  }
  .brand-dot { width: 30px; height: 30px; border-radius: 50%; background: var(--teal); }

  .slogan {
    position: absolute; left: 30px; top: 296px;
    font-family: "Bebas Neue", sans-serif; font-weight: 400; font-size: 42px; line-height: 46px;
    color: var(--paper); letter-spacing: .3px;
  }

  .headline {
    position: absolute; left: 100px; width: 500px; top: 494px;
    text-align: center;
    font-family: "Fira Sans", sans-serif; font-weight: 700;
    font-size: 34px; line-height: 46px; color: var(--teal-text);
  }

  .industries { position: absolute; left: 38px; top: 622px; width: 310px; }
  .industries-title {
    font-family: "Bebas Neue", sans-serif; font-weight: 400; font-size: 31px; color: var(--green);
    letter-spacing: .3px; line-height: 34px;
  }
  .industries-rule { width: 78px; height: 2px; background: var(--teal); margin: 4px 0 12px; }
  .industries-list {
    list-style: none; display: grid; grid-template-columns: 154px 150px;
    row-gap: 11px;
    font-size: 19px; color: var(--ink-soft);
  }
  .industries-list li { display: flex; align-items: center; gap: 8px; height: 22px; white-space: nowrap; }
  .tick { width: 16px; height: 16px; flex: none; }

  .about {
    position: absolute; left: 368px; top: 620px; width: 293px;
    font-family: "Lato", sans-serif; font-size: 11.6px; line-height: 17px;
    color: var(--ink); text-align: justify;
  }
  .about-claim {
    margin-top: 10px;
    font-family: "Fira Sans", sans-serif; font-weight: 600;
    color: var(--teal-text); font-size: 12px;
  }

  .contact-tab {
    position: absolute; left: 64px; top: 796px;
    font-family: "Bebas Neue", sans-serif; font-size: 27px; line-height: 34px; color: var(--paper);
    letter-spacing: .3px;
  }
  .contact-row {
    position: absolute; left: 72px; top: 840px;
    display: flex; align-items: center; gap: 20px;
    font-family: "Fira Sans", sans-serif; font-weight: 600; font-size: 13.5px;
    color: var(--paper); white-space: nowrap;
  }
  .contact-item { display: flex; align-items: center; gap: 7px; }
  .contact-icon { width: 17px; height: 17px; flex: none; }
</style>
</head>
<body>
<main class="flyer">
  <svg class="artwork" viewBox="0 0 696 900">
    <defs>
      <linearGradient id="scene-sky" x1="0" y1="0" x2="0" y2="1">
        <stop offset="0" stop-color="var(--sky-1)"/>
        <stop offset=".28" stop-color="var(--sky-2)"/>
        <stop offset=".42" stop-color="var(--roof)"/>
        <stop offset=".62" stop-color="var(--wall)"/>
        <stop offset=".82" stop-color="var(--lamp)"/>
        <stop offset="1" stop-color="#8b7a66"/>
      </linearGradient>
      <radialGradient id="scene-suit" cx=".82" cy=".42" r=".42">
        <stop offset="0" stop-color="var(--suit)" stop-opacity=".95"/>
        <stop offset=".6" stop-color="var(--suit)" stop-opacity=".45"/>
        <stop offset="1" stop-color="var(--suit)" stop-opacity="0"/>
      </radialGradient>
      <linearGradient id="circle-a" x1="0" y1="0" x2="0" y2="1">
        <stop offset="0" stop-color="#c9d6e2"/>
        <stop offset=".55" stop-color="#e8edf2"/>
        <stop offset="1" stop-color="#7f8e9e"/>
      </linearGradient>
      <linearGradient id="circle-b" x1="0" y1="0" x2="1" y2="1">
        <stop offset="0" stop-color="#eef2f6"/>
        <stop offset=".6" stop-color="#d7dfe7"/>
        <stop offset="1" stop-color="#4fa96a"/>
      </linearGradient>
      <linearGradient id="circle-c" x1="0" y1="0" x2="0" y2="1">
        <stop offset="0" stop-color="#d9e3ec"/>
        <stop offset=".5" stop-color="#f1f4f7"/>
        <stop offset="1" stop-color="#b7c2cc"/>
      </linearGradient>
      <linearGradient id="haze" x1="0" y1="0" x2="0" y2="1">
        <stop offset="0" stop-color="#bfe6df" stop-opacity=".9"/>
        <stop offset="1" stop-color="#ffffff" stop-opacity="0"/>
      </linearGradient>
    </defs>

    <g role="img" aria-label="Photo of a worker in white coveralls and mask spraying disinfectant in front of a large suburban house at dusk">
      <polygon points="446,0 696,0 696,503 307,397 0,213" fill="url(#scene-sky)"/>
      <polygon points="446,0 696,0 696,503 307,397 0,213" fill="url(#scene-suit)"/>
    </g>
    <polygon points="0,528 696,420 696,600 0,600" fill="url(#haze)"/>
    <polygon class="slogan-panel" points="0,213 307,397 0,528" fill="var(--teal)"/>

    <g role="img" aria-label="Photo of a technician in protective gear spraying a room">
      <circle cx="339" cy="351" r="53" fill="url(#circle-a)" stroke="#ffffff" stroke-width="3"/>
    </g>
    <g role="img" aria-label="Photo of a worker in coveralls holding a green sprayer">
      <circle cx="466" cy="397" r="64" fill="url(#circle-b)" stroke="#ffffff" stroke-width="3"/>
    </g>
    <g role="img" aria-label="Photo of a disinfection team walking through a bright hallway">
      <circle cx="606" cy="458" r="75" fill="url(#circle-c)" stroke="#ffffff" stroke-width="3"/>
    </g>

    <polygon class="contact-band" points="18,806 675,806 663,870 12,870" fill="var(--teal)"/>
    <polygon class="contact-tab-shape" points="32,794 287,794 296,830 26,830" fill="var(--green-soft)"/>
    <polygon points="26,830 32,794 28,794 22,830" fill="var(--teal-deep)"/>
  </svg>

  <div class="brand"><span class="brand-name">KLENVO</span><span class="brand-dot"></span></div>

  <h2 class="slogan">Disinfect<br>Today for a safe<br>Tomorrow</h2>

  <h1 class="headline">CORONAVIRUS<br>DESINFECTING SERVICES</h1>

  <section class="industries">
    <h3 class="industries-title">Industries we serve</h3>
    <div class="industries-rule"></div>
    <ul class="industries-list">
      <li><svg class="tick" viewBox="0 0 16 16"><rect x="1.5" y="2.5" width="12" height="12" rx="2" fill="none" stroke="var(--teal)" stroke-width="1.6"/><path d="M4.5 8.5l3 3 7-8" fill="none" stroke="var(--teal)" stroke-width="2"/></svg>Food Service</li>
      <li><svg class="tick" viewBox="0 0 16 16"><rect x="1.5" y="2.5" width="12" height="12" rx="2" fill="none" stroke="var(--teal)" stroke-width="1.6"/><path d="M4.5 8.5l3 3 7-8" fill="none" stroke="var(--teal)" stroke-width="2"/></svg>Laundry</li>
      <li><svg class="tick" viewBox="0 0 16 16"><rect x="1.5" y="2.5" width="12" height="12" rx="2" fill="none" stroke="var(--teal)" stroke-width="1.6"/><path d="M4.5 8.5l3 3 7-8" fill="none" stroke="var(--teal)" stroke-width="2"/></svg>Hospitality</li>
      <li><svg class="tick" viewBox="0 0 16 16"><rect x="1.5" y="2.5" width="12" height="12" rx="2" fill="none" stroke="var(--teal)" stroke-width="1.6"/><path d="M4.5 8.5l3 3 7-8" fill="none" stroke="var(--teal)" stroke-width="2"/></svg>Food Plants</li>
      <li><svg class="tick" viewBox="0 0 16 16"><rect x="1.5" y="2.5" width="12" height="12" rx="2" fill="none" stroke="var(--teal)" stroke-width="1.6"/><path d="M4.5 8.5l3 3 7-8" fill="none" stroke="var(--teal)" stroke-width="2"/></svg>Healthcare</li>
      <li><svg class="tick" viewBox="0 0 16 16"><rect x="1.5" y="2.5" width="12" height="12" rx="2" fill="none" stroke="var(--teal)" stroke-width="1.6"/><path d="M4.5 8.5l3 3 7-8" fill="none" stroke="var(--teal)" stroke-width="2"/></svg>Institutions</li>
    </ul>
  </section>

  <section class="about">
    <p>We will be offering a service where we go into facilities like residential, office, child care, medical, dental, restaurant, entertainment, hotel/motel, automotive fleets with professional spraying equipment and disinfect their facilities for a fee.</p>
    <p class="about-claim">Our products kills a wide range of viruses and pathogens including Covid 19.</p>
  </section>

  <div class="contact-tab">Contact us now!!</div>
  <div class="contact-row">
    <span class="contact-item"><svg class="contact-icon" viewBox="0 0 18 18"><circle cx="9" cy="9" r="9" fill="var(--green)"/><rect x="4.5" y="6" width="9" height="6.5" fill="none" stroke="#fff" stroke-width="1.2"/><path d="M4.5 6l4.5 3.8L13.5 6" fill="none" stroke="#fff" stroke-width="1.2"/></svg>klenvotrue@mailbox-example.com</span>
    <span class="contact-item"><svg class="contact-icon" viewBox="0 0 18 18"><circle cx="9" cy="9" r="9" fill="var(--green)"/><circle cx="9" cy="9" r="5" fill="none" stroke="#fff" stroke-width="1.1"/><ellipse cx="9" cy="9" rx="2.2" ry="5" fill="none" stroke="#fff" stroke-width="1.1"/><path d="M4 9h10" stroke="#fff" stroke-width="1.1"/></svg>www.klenvo-example.com</span>
    <span class="contact-item"><svg class="contact-icon" viewBox="0 0 18 18"><circle cx="9" cy="9" r="9" fill="var(--green)"/><path d="M6 4.5l2 2.3-1.1 1.3a7 7 0 0 0 3 3l1.3-1.1 2.3 2-1 1.6c-4 .3-8-3.7-7.7-7.7z" fill="#fff"/></svg>905-487-2963</span>
  </div>
</main>
</body>
</html>
```